Business Card Design Project for Architecture and Interior Design company

We need a business card design and logo for an architecture and design firm located in Santiago de Chile. It´s a small company, and the name is "Ostrevo" ("Ostr" from my surname Ostrini, and "arq" for arquitectura or architecture. But it would also be nice that the logo comunicates de Word game "Bella" as beautiful in italian, and "arq" as architecture".
The idea is to give a delicate, elegant and sofisticated, yet fresh image. Would prefer grey black and white colors, but wouldn´t mind to use another additional color.
I allready have a web page www.ostrevo-studio.example, but would like to improve the logo design.
Please contact if any further information is requiered.
Reason: Need a more arquitectural and desing spirit in the cards. Few of them give that idea.

```html
<!DOCTYPE html>
<html lang="en">
<head>
<meta charset="utf-8">
<title>Ostrevo — Business Cards</title>
<link rel="stylesheet" href="https://fonts.googleapis.com/css2?family=Ubuntu:wght@400;700&display=swap">
<style>
  :root {
    --backdrop: #2a2a2a;
    --card-white: #f2f2f2;
    --card-dark: #1e1c1c;
    --accent-red: #d42a22;
    --ink: #1b1b1b;
    --ink-soft: #333;
    --ghost-grey: #a9a9a9;
  }
  * { margin: 0; padding: 0; box-sizing: border-box; }
  html, body {
    width: 1200px; height: 900px; overflow: hidden;
    background: var(--backdrop);
    font-family: "Ubuntu", sans-serif;
  }
  .canvas { position: relative; width: 1200px; height: 900px; }
  .card {
    position: absolute; width: 620px; height: 350px;
    overflow: hidden; background: var(--card-white);
    box-shadow: 0 12px 30px rgba(0,0,0,.5);
  }
  .card-shape { position: absolute; inset: 0; width: 100%; height: 100%; z-index: 1; }
  .card-front { left: 110px; top: 80px; }
  .card-back { left: 470px; top: 470px; }

  .front-brand {
    position: absolute; left: 0; right: 0; top: 112px;
    text-align: center; z-index: 2;
  }
  .brand-name {
    font-weight: 700; font-size: 96px; line-height: 1;
    color: var(--ink); letter-spacing: -2px;
  }
  .brand-web {
    margin-top: 10px;
    font-weight: 700; font-size: 24px; color: var(--ink);
    letter-spacing: 1px;
  }

  .holder {
    position: absolute; right: 40px; top: 34px; text-align: right; z-index: 2;
  }
  .holder-name { font-size: 27px; color: var(--ink); letter-spacing: 1px; }
  .holder-role { font-size: 20px; color: var(--ink-soft); margin-top: 2px; }

  .contact {
    position: absolute; display: flex; align-items: center; gap: 10px;
    font-size: 14px; color: var(--ink-soft); letter-spacing: .4px; z-index: 2;
    white-space: nowrap;
  }
  .contact-mail { left: 280px; top: 128px; }
  .contact-phone { left: 60px; top: 184px; }
  .contact-icon { width: 22px; height: 22px; flex: none; }

  .ghost-brand {
    position: absolute; left: 18px; bottom: -26px; z-index: 0;
    font-weight: 700; font-size: 120px; line-height: 1;
    color: var(--ghost-grey); letter-spacing: -4px;
  }
</style>
</head>
<body>
<main class="canvas">

  <section class="card card-front" aria-label="Card front">
    <svg class="card-shape" viewBox="0 0 620 350" aria-hidden="true">
      <path d="M0 60 Q70 250 0 350 Z" fill="var(--card-dark)"/>
      <path d="M0 60 Q70 250 0 350" fill="none" stroke="var(--accent-red)" stroke-width="4"/>
      <path d="M480 0 Q640 40 620 200 L620 0 Z" fill="var(--card-dark)"/>
      <path d="M480 0 Q640 40 620 200" fill="none" stroke="var(--accent-red)" stroke-width="4"/>
    </svg>
    <div class="front-brand">
      <div class="brand-name">ostrevo</div>
      <div class="brand-web">www.ostrevo-studio.example</div>
    </div>
  </section>

  <section class="card card-back" aria-label="Card back">
    <div class="ghost-brand">ostrevo</div>
    <svg class="card-shape" viewBox="0 0 620 350" aria-hidden="true">
      <path d="M490 350 Q605 300 620 180 L620 350 Z" fill="var(--card-dark)"/>
      <path d="M490 350 Q605 300 620 180" fill="none" stroke="var(--accent-red)" stroke-width="4"/>
    </svg>

    <div class="holder">
      <div class="holder-name">MIRA OSTRINI DELCOR</div>
      <div class="holder-role">Arquitecto</div>
    </div>

    <div class="contact contact-mail">
      <svg class="contact-icon" viewBox="0 0 22 22" aria-hidden="true">
        <circle cx="11" cy="11" r="10" fill="var(--accent-red)" stroke="var(--ink)" stroke-width="1.5"/>
        <rect x="5.5" y="7.5" width="11" height="7.5" fill="#fff"/>
        <path d="M5.5 7.5 L11 12 L16.5 7.5" fill="none" stroke="var(--accent-red)" stroke-width="1"/>
      </svg>
      <span>mostrini@ostrevo-studio.example</span>
    </div>

    <div class="contact contact-phone">
      <svg class="contact-icon" viewBox="0 0 22 22" aria-hidden="true">
        <circle cx="11" cy="11" r="10" fill="var(--accent-red)" stroke="var(--ink)" stroke-width="1.5"/>
        <path d="M7.5 6 L9.5 6 L10.3 8.6 L9 9.6 Q10 12 12.4 13 L13.4 11.7 L16 12.5 L16 14.5 Q15 16 13 15.6 Q7.8 14 6.4 8.6 Q6.2 6.8 7.5 6 Z" fill="#fff"/>
      </svg>
      <span>+56 9 5550 1234</span>
    </div>
  </section>

</main>
</body>
</html>
```